Redesign of PTO Calendar website

Looking to drastically improve our PTO (paid time off) Calendar look and feel. Need a modern and well thought out design that is fun.
Current Screenshots
https://files.brindlemoor.net/sheet/p/7vTq2LmW9xZpK4nRb8JsYcHa3eDfG5uNwQ1tVhXo/view?mode=public
It's written in PHP and Laravel, if that matters. I am not necessarily attached to any of the current design, so please go wild. Current functionality needs to remain the same, but some can be added if you feel it would be of value. Layout can certainly change.
NOTE - this calendar can be used by any company, not just our own. So we'd like it to have a look and feel that is easy to navigate.
Site logo is attached.
Pages needed:
* Login Page
* Registration Page
* Calendar page
* Add PTO method
* Admin page (will use template for all admin areas)
* User profile page
Thanks!

```html
<!DOCTYPE html>
<html lang="en">
<head>
<meta charset="utf-8">
<title>Offday – Time Off Calendar</title>
<link href="https://fonts.googleapis.com/css2?family=Montserrat:wght@700;800&family=Nunito:wght@400;600;700&display=swap" rel="stylesheet">
<style>
:root{
  --blue:#0a74c2;
  --blue-dark:#075e9f;
  --ink:#2a3240;
  --muted:#7c8591;
  --faint:#c2c7ce;
  --line:#e3e6ea;
  --panel:#ffffff;
  --soft:#f4f6f8;
  --sidebar:#36404f;
  --green:#4cc17a;
  --red:#e5322d;
  --heading:#7d8590;
}
*{box-sizing:border-box;margin:0;padding:0}
html,body{width:1200px;height:3461px;overflow:hidden;background:#fff;font-family:"Nunito",sans-serif;color:var(--ink)}
.board{position:relative;width:1200px;height:3461px}
.section-title{position:absolute;left:0;width:1200px;height:75px;display:flex;align-items:center;justify-content:center;gap:14px;font-family:"Montserrat",sans-serif;font-weight:800;font-size:25px;color:var(--heading);letter-spacing:.5px}
.section-title::before{content:"";width:8px;height:30px;background:var(--blue)}
.stage{position:absolute;left:0;width:1200px;overflow:hidden;
  background:
   radial-gradient(circle at 4% 18%, rgba(170,200,255,.75) 0 60px, rgba(190,210,255,.25) 95px, transparent 130px),
   radial-gradient(circle at 25% 12%, rgba(225,215,255,.8) 0, transparent 220px),
   radial-gradient(circle at 72% 8%, rgba(220,235,255,.9) 0, transparent 240px),
   radial-gradient(circle at 97% 40%, rgba(200,225,255,.9) 0 40px, transparent 150px),
   radial-gradient(circle at 90% 95%, rgba(255,255,255,.95) 0 90px, rgba(180,205,255,.5) 140px, transparent 200px),
   radial-gradient(circle at 18% 80%, rgba(255,255,255,.8) 0 70px, rgba(200,215,255,.4) 100px, transparent 140px),
   radial-gradient(circle at 62% 85%, rgba(210,240,215,.9) 0, transparent 260px),
   linear-gradient(120deg,#e6e9fb 0%,#f1f3fb 35%,#eef6ee 70%,#e7eefb 100%)}
/* login */
.login-card{position:absolute;left:312px;top:157px;width:562px;height:439px;background:rgba(255,255,255,.55);border-radius:4px;box-shadow:0 4px 30px rgba(120,140,180,.12)}
.brand{display:flex;align-items:center;gap:6px;font-family:"Montserrat",sans-serif;font-weight:800;color:var(--ink)}
.brand .dot{border-radius:50%;background:var(--blue)}
.login-card .brand{position:absolute;left:0;right:0;top:44px;justify-content:center;font-size:34px}
.login-card .brand .dot{width:26px;height:26px}
.field{position:absolute;left:63px;width:450px;height:54px;background:#fff;border-radius:3px;padding:0 16px;display:flex;align-items:center;font-size:17px;color:#4b5360}
.remember{position:absolute;left:63px;top:253px;width:450px;display:flex;align-items:center;font-size:17px;color:#4b5360}
.remember .box{width:28px;height:28px;background:#fff;margin-right:15px}
.remember a{margin-left:auto;color:var(--blue);text-decoration:none}
.login-btn{position:absolute;left:63px;top:293px;width:450px;height:56px;background:var(--blue);border-radius:3px;color:#fff;font-weight:700;font-size:17px;display:flex;align-items:center;justify-content:center;gap:10px;letter-spacing:.5px}
/* app frame */
.app{position:absolute;left:75px;width:1050px;height:640px;background:var(--soft);border-radius:22px;overflow:hidden;box-shadow:0 8px 30px rgba(100,120,160,.15)}
.topbar{position:absolute;left:0;top:0;width:100%;height:63px;background:#fff;border-bottom:1px solid var(--line)}
.topbar .brand{position:absolute;left:21px;top:17px;font-size:25px}
.topbar .brand .dot{width:20px;height:20px}
.search{position:absolute;left:667px;top:22px;display:flex;align-items:center;gap:6px;font-size:11px;color:var(--ink)}
.topbar .divider{position:absolute;left:833px;top:14px;width:1px;height:36px;background:var(--line)}
.bell{position:absolute;left:854px;top:20px}
.badge{position:absolute;left:865px;top:15px;width:13px;height:13px;border-radius:50%;background:var(--blue);color:#fff;font-size:8px;font-weight:700;display:flex;align-items:center;justify-content:center}
.avatar{border-radius:50%;background:radial-gradient(circle at 45% 40%,#d9b9a2 0 30%,#4d4440 60%,#2c2b30 100%)}
.topbar .avatar{position:absolute;left:895px;top:17px;width:30px;height:30px}
.user-name{position:absolute;left:937px;top:24px;font-size:11px;font-weight:600;display:flex;gap:10px;align-items:center}
.sidebar{position:absolute;left:0;top:63px;bottom:0;width:78px;background:var(--sidebar)}
.nav-icon{position:absolute;left:23px;width:32px;height:32px;display:flex;align-items:center;justify-content:center;border-radius:5px}
.nav-icon.active{background:var(--blue)}
.tooltip{position:absolute;left:50px;width:83px;height:22px;background:#fff;border-radius:11px;font-size:10px;display:flex;align-items:center;justify-content:center;box-shadow:0 2px 6px rgba(0,0,0,.15)}
.cursor{position:absolute}
/* calendar */
.event-card{position:absolute;left:112px;top:101px;width:188px;height:149px;background:#fff;border-radius:3px}
.event-card h3{height:30px;background:#eceef1;font-size:14px;font-weight:600;display:flex;align-items:center;justify-content:center}
.event-row{display:flex;align-items:center;gap:12px;padding:12px 0 0 20px;font-size:11px;font-weight:600;line-height:1.3}
.event-row .avatar{width:28px;height:28px;position:relative}
.event-row .avatar::after{content:"";position:absolute;right:-2px;bottom:-1px;width:9px;height:9px;border-radius:50%;background:#f0566a}
.cal-panel{position:absolute;left:323px;top:101px;width:689px;height:501px;background:#fff;border-radius:3px}
.arrow{position:absolute;top:20px;width:26px;height:26px;border-radius:3px;background:#eceef1;display:flex;align-items:center;justify-content:center}
.today{position:absolute;left:106px;top:23px;font-size:10px;line-height:1.25}
.month{position:absolute;left:0;width:689px;top:24px;text-align:center;font-size:15px;font-weight:600;padding-left:0}
.views{position:absolute;left:503px;top:20px;width:157px;height:29px;border:1px solid var(--line);border-radius:3px;display:flex;font-size:10px}
.views span{flex:1;display:flex;align-items:center;justify-content:center}
.views .on{background:#e8ebef}
.grid{position:absolute;left:30px;top:69px;width:630px;border:1px solid var(--line);border-radius:4px;overflow:hidden}
.grid .head{display:grid;grid-template-columns:repeat(7,90px);height:35px;background:#eceef1;font-size:11px}
.grid .head span{display:flex;align-items:center;justify-content:center}
.days{position:relative;display:grid;grid-template-columns:repeat(7,90px);grid-auto-rows:75px}
.days span{border-right:1px solid var(--line);border-bottom:1px solid var(--line);font-size:9px;text-align:right;padding:2px 5px}
.days span.out{color:var(--faint)}
.pto{position:absolute;background:var(--green);color:#fff;font-size:9px;display:flex;align-items:center;justify-content:center;line-height:1.4}
/* modal */
.dim{position:absolute;left:0;top:63px;right:0;bottom:0;background:rgba(72,82,100,.78)}
.modal{position:absolute;left:236px;top:142px;width:562px;height:437px;background:#f2f3f5;border-radius:3px}
.modal h2{position:absolute;left:0;right:0;top:24px;text-align:center;font-size:19px;font-weight:600}
.close{position:absolute;right:22px;top:22px}
.modal label{position:absolute;left:63px;font-size:14px;font-weight:600}
.input{position:absolute;left:63px;width:450px;height:40px;background:#fff;border-radius:3px;padding:0 16px;display:flex;align-items:center;justify-content:space-between;font-size:15px}
.btn{position:absolute;top:367px;width:219px;height:42px;border-radius:3px;display:flex;align-items:center;justify-content:center;font-weight:700;font-size:15px;letter-spacing:.5px}
.btn.save{left:63px;background:var(--blue);color:#fff}
.btn.cancel{left:294px;border:1px solid var(--blue);color:var(--blue);background:#fff}
/* admin */
.admin-panel{position:absolute;left:112px;top:101px;width:900px;height:415px;background:#fff;border-radius:3px}
.show{position:absolute;left:32px;top:22px;display:flex;align-items:center;gap:12px;font-size:10px}
.show .select{width:60px;height:28px;background:#eceef1;border-radius:3px;display:flex;align-items:center;justify-content:space-around}
.search-box{position:absolute;left:711px;top:20px;width:158px;height:30px;border:1px solid var(--line);border-radius:3px;font-size:10px;display:flex;align-items:center;justify-content:space-between;padding:0 10px}
table{position:absolute;left:32px;top:68px;width:839px;border-collapse:collapse;font-size:10px}
th{height:35px;background:#eceef1;font-weight:600;text-align:left;padding-left:22px}
td{height:75px;border-bottom:1px solid var(--line);border-right:1px solid var(--line);padding:0 22px;font-weight:600}
td:last-child{border-right:none}
td.desc{font-size:9px;line-height:1.2;padding:0 18px 0 22px}
td.num{text-align:center;padding:0}
.status{display:flex;align-items:center;gap:6px}
.tick{width:14px;height:14px;border-radius:2px;background:var(--green);display:flex;align-items:center;justify-content:center}
.edit{color:var(--blue);margin-right:14px}
.delete{color:var(--red)}
.entries{position:absolute;left:32px;top:352px;font-size:10px;font-weight:600}
.pager{position:absolute;left:711px;top:350px;width:157px;height:28px;border:1px solid var(--line);border-radius:3px;display:flex;font-size:10px}
.pager span{flex:1;display:flex;align-items:center;justify-content:center}
.pager .cur{background:#eceef1}
</style>
</head>
<body>
<div class="board">

<!-- LOGIN -->
<div class="section-title" style="top:0">LOGIN</div>
<section class="stage" style="top:75px;height:713px">
  <div class="login-card">
    <div class="brand">Offday<span class="dot"></span></div>
    <div class="field" style="top:117px">Email Address</div>
    <div class="field" style="top:185px">Password</div>
    <div class="remember"><span class="box"></span>Remember me<a href="#">Forgot password?</a></div>
    <div class="login-btn">
      <svg width="14" height="16" viewBox="0 0 14 16" fill="none" stroke="#fff" stroke-width="1.5"><rect x="1" y="7" width="12" height="8" rx="1.5"/><path d="M4 7V4.5a3 3 0 0 1 6 0V7"/></svg>LOGIN
    </div>
  </div>
</section>

<!-- CALENDAR -->
<div class="section-title" style="top:788px">CALENDAR</div>
<section class="stage" style="top:863px;height:790px">
  <div class="app" style="top:75px">
    <div class="topbar">
      <div class="brand">Offday<span class="dot"></span></div>
      <div class="search"><svg width="17" height="17" viewBox="0 0 17 17" fill="none" stroke="#2a3240" stroke-width="2"><circle cx="7" cy="7" r="5.5"/><path d="M11 11l4.5 4.5"/></svg>Type to search here...</div>
      <div class="divider"></div>
      <svg class="bell" width="18" height="20" viewBox="0 0 18 20" fill="none" stroke="#2a3240" stroke-width="1.5"><path d="M3 15V9a6 6 0 0 1 12 0v6l1.5 1.5h-15z"/><path d="M7 18.5h4"/></svg>
      <span class="badge">3</span>
      <div class="avatar" role="img" aria-label="User portrait"></div>
      <div class="user-name">Milo Brennan <svg width="8" height="5" viewBox="0 0 8 5" fill="none" stroke="#9aa1aa"><path d="M1 1l3 3 3-3"/></svg></div>
    </div>
    <div class="sidebar">
      <div class="nav-icon" style="top:16px"><svg width="18" height="18" viewBox="0 0 18 18" fill="none" stroke="#fff" stroke-width="1.5"><path d="M2 8l7-6 7 6v8H2z"/><path d="M7 16v-5h4v5"/></svg></div>
      <div class="nav-icon" style="top:58px"><svg width="20" height="14" viewBox="0 0 20 14" fill="#fff"><circle cx="10" cy="4" r="3"/><circle cx="4" cy="5" r="2.2"/><circle cx="16" cy="5" r="2.2"/><path d="M5 13a5 5 0 0 1 10 0z"/><path d="M0 13a4 4 0 0 1 6-3.5V13zM20 13a4 4 0 0 0-6-3.5V13z"/></svg></div>
      <div class="nav-icon" style="top:98px"><svg width="16" height="18" viewBox="0 0 16 18" fill="#fff"><circle cx="8" cy="5" r="4.5"/><path d="M0 18a8 7 0 0 1 16 0z"/></svg></div>
      <div class="nav-icon" style="top:140px"><svg width="14" height="18" viewBox="0 0 14 18" fill="none" stroke="#fff" stroke-width="1.5"><path d="M1 1h12v16l-6-4-6 4z"/></svg></div>
      <div class="nav-icon active" style="top:181px"><svg width="18" height="18" viewBox="0 0 18 18" fill="none" stroke="#fff" stroke-width="1.5"><rect x="1" y="3" width="16" height="14" rx="1.5"/><path d="M1 7h16M5 1v4M13 1v4M5 10h2M9 10h2M13 10h1M5 13h2M9 13h2"/></svg></div>
      <div class="tooltip" style="top:166px">Add PTO</div>
      <svg class="cursor" style="left:38px;top:198px" width="16" height="22" viewBox="0 0 16 22"><path d="M1 1v17l4-4 3 7 3-1-3-7h6z" fill="#fff" stroke="#2a3240" stroke-width="1.2"/></svg>
    </div>
    <div class="event-card">
      <h3>Today's Event (1)</h3>
      <div class="event-row"><div class="avatar" role="img" aria-label="Team member portrait"></div><div>Milo Brennan<br>Vacation</div></div>
    </div>
    <div class="cal-panel">
      <div class="arrow" style="left:31px"><svg width="8" height="12" viewBox="0 0 8 12" fill="none" stroke="#2a3240" stroke-width="2"><path d="M6 1L1.5 6 6 11"/></svg></div>
      <div class="arrow" style="left:65px"><svg width="8" height="12" viewBox="0 0 8 12" fill="none" stroke="#2a3240" stroke-width="2"><path d="M2 1l4.5 5L2 11"/></svg></div>
      <div class="today">Today<br>August 22, 2020</div>
      <div class="month">August 2020</div>
      <div class="views"><span class="on">Month</span><span>Week</span><span>Day</span></div>
      <div class="grid">
        <div class="head"><span>Sun</span><span>Mon</span><span>Tue</span><span>Wed</span><span>Thu</span><span>Fri</span><span>Sat</span></div>
        <div class="days">
          <span class="out">29</span><span class="out">30</span><span class="out">31</span><span>1</span><span>2</span><span>3</span><span>4</span>
          <span>5</span><span>6</span><span>7</span><span>8</span><span>9</span><span>10</span><span>11</span>
          <span>12</span><span>13</span><span>14</span><span>15</span><span>16</span><span>17</span><span>18</span>
          <span>19</span><span>20</span><span>21</span><span>22</span><span>23</span><span>24</span><span>25</span>
          <span>26</span><span>27</span><span>28</span><span>29</span><span>30</span><span>31</span><span class="out">1</span>
          <div class="pto" style="left:180px;top:75px;width:180px;height:75px">12A - Owen Brennan Vacation<br>4A - Tessa Marlow Vacation</div>
          <div class="pto" style="left:540px;top:150px;width:90px;height:75px"></div>
          <div class="pto" style="left:0;top:225px;width:270px;height:75px">12A - Milo Brennan Vacation</div>
        </div>
      </div>
    </div>
  </div>
</section>

<!-- ADD PTO -->
<div class="section-title" style="top:1653px">ADD PTO</div>
<section class="stage" style="top:1728px;height:792px">
  <div class="app" style="top:76px">
    <div class="topbar">
      <div class="brand">Offday<span class="dot"></span></div>
      <div class="search"><svg width="17" height="17" viewBox="0 0 17 17" fill="none" stroke="#2a3240" stroke-width="2"><circle cx="7" cy="7" r="5.5"/><path d="M11 11l4.5 4.5"/></svg>Type to search here...</div>
      <div class="divider"></div>
      <svg class="bell" width="18" height="20" viewBox="0 0 18 20" fill="none" stroke="#2a3240" stroke-width="1.5"><path d="M3 15V9a6 6 0 0 1 12 0v6l1.5 1.5h-15z"/><path d="M7 18.5h4"/></svg>
      <span class="badge">3</span>
      <div class="avatar" role="img" aria-label="User portrait"></div>
      <div class="user-name">Milo Brennan <svg width="8" height="5" viewBox="0 0 8 5" fill="none" stroke="#9aa1aa"><path d="M1 1l3 3 3-3"/></svg></div>
    </div>
    <div class="sidebar">
      <div class="nav-icon" style="top:16px"><svg width="18" height="18" viewBox="0 0 18 18" fill="none" stroke="#fff" stroke-width="1.5"><path d="M2 8l7-6 7 6v8H2z"/><path d="M7 16v-5h4v5"/></svg></div>
      <div class="nav-icon" style="top:58px"><svg width="20" height="14" viewBox="0 0 20 14" fill="#fff"><circle cx="10" cy="4" r="3"/><circle cx="4" cy="5" r="2.2"/><circle cx="16" cy="5" r="2.2"/><path d="M5 13a5 5 0 0 1 10 0z"/><path d="M0 13a4 4 0 0 1 6-3.5V13zM20 13a4 4 0 0 0-6-3.5V13z"/></svg></div>
      <div class="nav-icon" style="top:98px"><svg width="16" height="18" viewBox="0 0 16 18" fill="#fff"><circle cx="8" cy="5" r="4.5"/><path d="M0 18a8 7 0 0 1 16 0z"/></svg></div>
      <div class="nav-icon" style="top:140px"><svg width="14" height="18" viewBox="0 0 14 18" fill="none" stroke="#fff" stroke-width="1.5"><path d="M1 1h12v16l-6-4-6 4z"/></svg></div>
      <div class="nav-icon active" style="top:181px"><svg width="18" height="18" viewBox="0 0 18 18" fill="none" stroke="#fff" stroke-width="1.5"><rect x="1" y="3" width="16" height="14" rx="1.5"/><path d="M1 7h16M5 1v4M13 1v4"/></svg></div>
      <div class="tooltip" style="top:166px">Add PTO</div>
      <svg class="cursor" style="left:38px;top:198px" width="16" height="22" viewBox="0 0 16 22"><path d="M1 1v17l4-4 3 7 3-1-3-7h6z" fill="#fff" stroke="#2a3240" stroke-width="1.2"/></svg>
    </div>
    <div class="event-card">
      <h3>Today's Event (1)</h3>
      <div class="event-row"><div class="avatar" role="img" aria-label="Team member portrait"></div><div>Milo Brennan<br>Vacation</div></div>
    </div>
    <div class="cal-panel">
      <div class="today">Today<br>August 22, 2020</div>
      <div class="month">August 2020</div>
      <div class="views"><span class="on">Month</span><span>Week</span><span>Day</span></div>
      <div class="grid">
        <div class="head"><span>Sun</span><span>Mon</span><span>Tue</span><span>Wed</span><span>Thu</span><span>Fri</span><span>Sat</span></div>
        <div class="days">
          <span class="out">29</span><span class="out">30</span><span class="out">31</span><span>1</span><span>2</span><span>3</span><span>4</span>
          <span>5</span><span>6</span><span>7</span><span>8</span><span>9</span><span>10</span><span>11</span>
          <span>12</span><span>13</span><span>14</span><span>15</span><span>16</span><span>17</span><span>18</span>
          <span>19</span><span>20</span><span>21</span><span>22</span><span>23</span><span>24</span><span>25</span>
          <span>26</span><span>27</span><span>28</span><span>29</span><span>30</span><span>31</span><span class="out">1</span>
          <div class="pto" style="left:540px;top:150px;width:90px;height:75px"></div>
        </div>
      </div>
    </div>
    <div class="dim"></div>
    <div class="modal">
      <h2>ADD PTO</h2>
      <svg class="close" width="16" height="16" viewBox="0 0 16 16" stroke="#2a3240" stroke-width="2.5"><path d="M2 2l12 12M14 2L2 14"/></svg>
      <label style="top:67px">Member</label>
      <div class="input" style="top:90px">Milo Brennan<svg width="11" height="7" viewBox="0 0 11 7" fill="none" stroke="#2a3240" stroke-width="2"><path d="M1 1l4.5 4.5L10 1"/></svg></div>
      <label style="top:142px">PTO Type</label>
      <div class="input" style="top:165px">Vacation<svg width="11" height="7" viewBox="0 0 11 7" fill="none" stroke="#2a3240" stroke-width="2"><path d="M1 1l4.5 4.5L10 1"/></svg></div>
      <label style="top:217px">Start Date</label>
      <div class="input" style="top:240px">08/11/2020<svg width="17" height="17" viewBox="0 0 17 17" fill="none" stroke="#8a919b" stroke-width="1.2"><rect x="1" y="2.5" width="15" height="13.5" rx="1"/><path d="M1 6h15M5 1v3M12 1v3M4 9h2M8 9h2M12 9h1M4 12h2M8 12h2M12 12h1"/></svg></div>
      <label style="top:292px">Start Date</label>
      <div class="input" style="top:315px">08/14/2020<svg width="17" height="17" viewBox="0 0 17 17" fill="none" stroke="#8a919b" stroke-width="1.2"><rect x="1" y="2.5" width="15" height="13.5" rx="1"/><path d="M1 6h15M5 1v3M12 1v3M4 9h2M8 9h2M12 9h1M4 12h2M8 12h2M12 12h1"/></svg></div>
      <div class="btn save">SAVE</div>
      <div class="btn cancel">CANCEL</div>
    </div>
  </div>
</section>

<!-- GENERAL ADMIN -->
<div class="section-title" style="top:2520px">GENERAL ADMIN</div>
<section class="stage" style="top:2595px;height:792px">
  <div class="app" style="top:75px;height:642px">
    <div class="topbar">
      <div class="brand">Offday<span class="dot"></span></div>
      <div class="search"><svg width="17" height="17" viewBox="0 0 17 17" fill="none" stroke="#2a3240" stroke-width="2"><circle cx="7" cy="7" r="5.5"/><path d="M11 11l4.5 4.5"/></svg>Type to search here...</div>
      <div class="divider"></div>
      <svg class="bell" width="18" height="20" viewBox="0 0 18 20" fill="none" stroke="#2a3240" stroke-width="1.5"><path d="M3 15V9a6 6 0 0 1 12 0v6l1.5 1.5h-15z"/><path d="M7 18.5h4"/></svg>
      <span class="badge">3</span>
      <div class="avatar" role="img" aria-label="User portrait"></div>
      <div class="user-name">Milo Brennan <svg width="8" height="5" viewBox="0 0 8 5" fill="none" stroke="#9aa1aa"><path d="M1 1l3 3 3-3"/></svg></div>
    </div>
    <div class="sidebar">
      <div class="nav-icon" style="top:16px"><svg width="18" height="18" viewBox="0 0 18 18" fill="none" stroke="#fff" stroke-width="1.5"><path d="M2 8l7-6 7 6v8H2z"/><path d="M7 16v-5h4v5"/></svg></div>
      <div class="nav-icon active" style="top:58px"><svg width="20" height="14" viewBox="0 0 20 14" fill="#fff"><circle cx="10" cy="4" r="3"/><circle cx="4" cy="5" r="2.2"/><circle cx="16" cy="5" r="2.2"/><path d="M5 13a5 5 0 0 1 10 0z"/><path d="M0 13a4 4 0 0 1 6-3.5V13zM20 13a4 4 0 0 0-6-3.5V13z"/></svg></div>
      <div class="nav-icon" style="top:98px"><svg width="16" height="18" viewBox="0 0 16 18" fill="#fff"><circle cx="8" cy="5" r="4.5"/><path d="M0 18a8 7 0 0 1 16 0z"/></svg></div>
      <div class="nav-icon" style="top:140px"><svg width="14" height="18" viewBox="0 0 14 18" fill="none" stroke="#fff" stroke-width="1.5"><path d="M1 1h12v16l-6-4-6 4z"/></svg></div>
      <div class="nav-icon" style="top:181px"><svg width="18" height="18" viewBox="0 0 18 18" fill="none" stroke="#fff" stroke-width="1.5"><rect x="1" y="3" width="16" height="14" rx="1.5"/><path d="M1 7h16M5 1v4M13 1v4"/></svg></div>
      <div class="tooltip" style="top:166px">Add PTO</div>
      <svg class="cursor" style="left:38px;top:198px" width="16" height="22" viewBox="0 0 16 22"><path d="M1 1v17l4-4 3 7 3-1-3-7h6z" fill="#fff" stroke="#2a3240" stroke-width="1.2"/></svg>
    </div>
    <div class="admin-panel">
      <div class="show">Show <span class="select">20 <svg width="10" height="6" viewBox="0 0 10 6" fill="none" stroke="#2a3240" stroke-width="2"><path d="M1 1l4 4 4-4"/></svg></span></div>
      <div class="search-box">Search<svg width="12" height="12" viewBox="0 0 12 12" fill="none" stroke="#2a3240" stroke-width="1.5"><circle cx="5" cy="5" r="4"/><path d="M8 8l3 3"/></svg></div>
      <table>
        <colgroup><col style="width:117px"><col style="width:115px"><col style="width:251px"><col style="width:137px"><col style="width:102px"><col style="width:117px"></colgroup>
        <tr><th>Team Name</th><th>Supervisor</th><th>Team Description</th><th style="padding-left:24px">Resource Count</th><th>Status</th><th>New</th></tr>
        <tr><td>Nursing</td><td>Tessa Marlow</td><td class="desc">Lorem ipsum dolor sit amet, consectetur adipiscing elit, sed do eiusmod tempor incididunt ut labore et dolore magna ali qua ut enim ad minim veniam quis.</td><td class="num">0</td><td><span class="status"><span class="tick"><svg width="9" height="7" viewBox="0 0 9 7" fill="none" stroke="#fff" stroke-width="1.8"><path d="M1 3.5l2.5 2.5L8 1"/></svg></span>Active</span></td><td><span class="edit">Edit</span><span class="delete">Delete</span></td></tr>
        <tr><td>Medical</td><td>Jonah Brennan</td><td class="desc">Lorem ipsum dolor sit amet, consectetur adipiscing elit, sed do eiusmod tempor incididunt ut labore et dolore magna ali qua ut enim ad minim veniam quis.</td><td class="num">0</td><td><span class="status"><span class="tick"><svg width="9" height="7" viewBox="0 0 9 7" fill="none" stroke="#fff" stroke-width="1.8"><path d="M1 3.5l2.5 2.5L8 1"/></svg></span>Active</span></td><td><span class="edit">Edit</span><span class="delete">Delete</span></td></tr>
        <tr><td>Engineering</td><td>Tessa Marlow</td><td class="desc">Lorem ipsum dolor sit amet, consectetur adipiscing elit, sed do eiusmod tempor incididunt ut labore et dolore magna ali qua ut enim ad minim veniam quis.</td><td class="num">1</td><td><span class="status"><span class="tick"><svg width="9" height="7" viewBox="0 0 9 7" fill="none" stroke="#fff" stroke-width="1.8"><path d="M1 3.5l2.5 2.5L8 1"/></svg></span>Active</span></td><td><span class="edit">Edit</span><span class="delete">Delete</span></td></tr>
      </table>
      <div class="entries">Showing 1 to 3 of 3 entries</div>
      <div class="pager"><span>Prev</span><span class="cur">1</span><span>Next</span></div>
    </div>
  </div>
</section>

</div>
</body>
</html>
```